Online-Marketing Material für Verkäufer von Elektromaterial
Zielgruppe
Über Barnow:
Barnow ist ein dynamisches Unternehmen, das sich auf den Verkauf von Elektromaterial spezialisiert hat. Als Ihr digitaler Online-Butler für Elektromaterial bieten wir eine breite Palette von über 100.000 hochwertigen Produkten für Profis und Heimwerker. Von Kabeln und Schaltern bis zu modernen Photovoltaikanlagen – unsere Kunden finden bei uns alles, was sie für ihre Elektroprojekte benötigen.
Unser Name steht für:
Expertise in der Elektrobranche mit einem tiefgreifenden Verständnis für die Bedürfnisse unserer Kunden.
Leidenschaft für Elektrotechnik, die uns antreibt, stets innovative und hochwertige Produkte anzubieten.
Freundlichkeit im Kundenservice, denn wir stehen unseren Kunden mit Rat und Tat zur Seite.
Revolutionäre Ideen, mit denen wir die Elektroinstallation verbessern möchten.
Effiziente Lösungen, die Zeit sparen und den Aufwand minimieren.
Dauerhaftigkeit unserer Produkte, die zuverlässige und langanhaltende Installationen garantieren.
Wir sind nicht nur ein Elektromateriallieferant; wir sind Visionäre, die den Markt für Elektroinstallationen revolutionieren wollen. Unsere Marke repräsentiert Qualität, Innovation und eine zukunftsorientierte Denkweise. Wir streben danach, die Arbeit unserer Kunden einfacher, effizienter und erfolgreicher zu machen.
ZIELGRUPPE:
Die Zielgruppe von Barnow umfasst ein breites Spektrum an Kunden, die sich für Elektromaterial interessieren und dieses benötigen. Hier einige spezifische Details über die Zielgruppe:
Professionelle Elektroinstallateure:
Dies sind erfahrene Fachleute, die auf der Suche nach zuverlässigen, hochwertigen Elektroinstallationsmaterialien für ihre tägliche Arbeit sind. Sie benötigen eine Quelle, die eine breite Palette von Produkten anbietet und die neuesten Technologien im Bereich der Elektroinstallation vorhält.
Bauunternehmen und Bauherren:
Große und kleine Bauunternehmen sowi..
Aufgabenstellung
Zweck:
Wir suchen talentierte Designer, die uns dabei helfen, eine Reihe von auffälligen und markengetreuen Social Media Designvorlagen zu erstellen, die für die Bewerbung unserer Produkte und Aktionen auf Trovanet und Pixmora verwendet werden können. Wir möchten Designs, die unsere Brandstory und unsere Ziele widerspiegeln und gleichzeitig flexibel genug sind, um für verschiedene Kampagnen und saisonale Ereignisse wie Mega Montag, Klickwoche oder DIY-Wochen eingesetzt zu werden.
Anforderungen:
Markenfarben: Bitte verwenden Sie die durch unser Logo vorgegebenen Markenfarben. Wir sind offen für die Integration von komplementären Farben, solange diese das Gesamtbild unterstützen und die Markenidentität stärken.
Formate: Ihre Designs sollten für die folgenden Formate optimiert sein:
Trovanet und Pixmora Stories
Trovanet und Pixmora Postings (inklusive Carrousel-Posts)
Pixmora Reels Ads
Inhalte: Wir ermutigen die Verwendung von Stockbildern, die mit unserer Branche und unseren Produkten in Verbindung stehen, wie Lampen, PV-Module, Schalter, Kabel und Leuchtmittel. Die Bilder sollten hochwertig sein und die Professionalität und Qualität unserer Marke widerspiegeln.
Anpassbarkeit: Die Designs sollten einfach anzupassen sein, um Textänderungen oder das Hinzufügen neuer Inhalte zu ermöglichen, ohne dass das Gesamtdesign neu gestaltet werden muss.
Innovation: Wir ermutigen Kreativität und Originalität – denken Sie über den Tellerrand hinaus! Wenn Sie Ideen haben, die über Trovanet und Pixmora hinausgehen, freuen wir uns darauf, diese zu sehen.
Abgabe: Bitte liefern Sie ein Komplettpaket, das Vorlagen für alle genannten Formate enthält. Wir möchten die Designs in editierbaren Dateien erhalten, damit wir sie bei Bedarf intern anpassen können.

```html
<!DOCTYPE html>
<html lang="de">
<head>
<meta charset="utf-8">
<title>Barnow – Online Shop</title>
<link rel="stylesheet" href="https://fonts.googleapis.com/css2?family=Roboto:wght@300;400;500;700;900&display=swap">
<style>
  :root {
    --teal: #13a59b;
    --accent-cyan: #19f2ec;
    --ink: #0b0b0b;
    --wordmark: #3a3f44;
    --white: #ffffff;
    --sky: #a9c4cf;
    --haze: #d9dcd6;
    --ground: #3f5258;
  }
  html, body {
    margin: 0;
    padding: 0;
    width: 1200px;
    height: 1200px;
    overflow: hidden;
    background: var(--white);
  }
  .ad {
    position: relative;
    width: 1200px;
    height: 1200px;
    overflow: hidden;
    font-family: "Roboto", Arial, sans-serif;
    color: var(--ink);
  }
  .ad__photo {
    position: absolute;
    inset: 0;
    background:
      radial-gradient(circle at 1000px 640px, rgba(255,214,110,0.95) 0, rgba(241,178,60,0.7) 140px, rgba(241,178,60,0) 420px),
      linear-gradient(180deg, var(--sky) 0%, #c4d3d6 35%, var(--haze) 55%, #8f9a92 78%, var(--ground) 100%);
  }
  .ad__fade {
    position: absolute;
    inset: 0;
    background: linear-gradient(90deg, rgba(255,255,255,0.97) 0%, rgba(255,255,255,0.85) 22%, rgba(255,255,255,0.35) 48%, rgba(255,255,255,0) 70%);
  }
  .brand {
    position: absolute;
    left: 60px;
    top: 62px;
    display: flex;
    align-items: center;
    gap: 10px;
  }
  .brand__dot {
    width: 92px;
    height: 92px;
    border-radius: 50%;
    background: var(--teal);
  }
  .brand__name {
    font-weight: 700;
    font-size: 38px;
    letter-spacing: 3px;
    color: var(--wordmark);
    line-height: 1;
  }
  .brand__tagline {
    margin-top: 8px;
    font-weight: 400;
    font-size: 15px;
    letter-spacing: 2.2px;
    line-height: 1.35;
    color: var(--wordmark);
  }
  .kicker {
    position: absolute;
    left: 58px;
    top: 362px;
    margin: 0;
    font-weight: 300;
    font-size: 27px;
    letter-spacing: 1px;
  }
  .headline {
    position: absolute;
    left: 50px;
    top: 430px;
    margin: 0;
    font-weight: 900;
    font-size: 86px;
    line-height: 83px;
    letter-spacing: 1.5px;
  }
  .headline__slash {
    display: inline-block;
    width: 17px;
    height: 60px;
    margin-left: 22px;
    background: var(--accent-cyan);
    transform: skewX(-22deg);
    vertical-align: -2px;
  }
  .cta {
    position: absolute;
    left: 53px;
    top: 955px;
    width: 389px;
    height: 94px;
    border-radius: 26px;
    background: var(--teal);
    color: var(--white);
    display: flex;
    align-items: center;
    justify-content: center;
    font-weight: 700;
    font-size: 25px;
    letter-spacing: 0.8px;
    text-decoration: none;
  }
  .web {
    position: absolute;
    left: 69px;
    top: 1086px;
    display: flex;
    align-items: center;
    gap: 18px;
    font-weight: 700;
    font-size: 27px;
    letter-spacing: 1px;
  }
  .web__icon { width: 58px; height: 58px; }
</style>
</head>
<body>
  <main class="ad">
    <div class="ad__photo" role="img" aria-label="Foto: Elektromonteure mit Helm klettern bei Sonnenuntergang an einem Strommast"></div>
    <div class="ad__fade"></div>

    <header class="brand">
      <div class="brand__dot"></div>
      <div>
        <div class="brand__name">BARNOW</div>
        <div class="brand__tagline">ELEKTROMATERIAL ONLINE<br>FÜR PROFIS &amp; HEIMWERKER</div>
      </div>
    </header>

    <p class="kicker">ONLINE SHOP</p>

    <h1 class="headline">
      MEHR ALS<br>
      WARE ZU LIEFERN,<br>
      HEIßT FÜR EUCH<br>
      DA ZU SEIN:<br>
      EGAL<br>
      WANN UND WO<span class="headline__slash"></span>
    </h1>

    <a class="cta" href="#">MEHR ERFAHREN!</a>

    <div class="web">
      <svg class="web__icon" viewBox="0 0 58 58" aria-hidden="true">
        <circle cx="29" cy="29" r="29" fill="#13a59b"/>
        <g fill="none" stroke="#ffffff" stroke-width="2.6">
          <circle cx="29" cy="29" r="18"/>
          <ellipse cx="29" cy="29" rx="8" ry="18"/>
          <line x1="11" y1="29" x2="47" y2="29"/>
          <line x1="14" y1="20" x2="44" y2="20"/>
          <line x1="14" y1="38" x2="44" y2="38"/>
        </g>
      </svg>
      <span>WWW.BARNOW.AT</span>
    </div>
  </main>
</body>
</html>
```